Business cards and stationery for dental surgery products company
Dental Crestline Works, LLC
Business cards and stationery for dental surgery products company - Medical
Creative Brief
Simple
Boris Kestrow
No address.
boris.kestrow@fernmail.example
Regenerative Products Surgical Supplies
Harbor Cell Providers - Quintara Ossel Vanta Spa, USA - Disposable Surgical Devices
bkestrow bkestrow
Designers - Thanks so much for all the concepts! The world is full of amazingly creative people! I apologize for not responding recently. The holidays go me behind at my work. Then my area of the US had a winter storm that knocked out my internet service for a couple of days. So, I have been playing catch up on my work and have failed to stay on top of this project. Here are a couple of items for everyone. My website will be - www.dentalcrestlineworks.example My Facebook info is - www.socialpage.example/dentalcrestlineworks. Also, this will be my primary online vehicle. I will use it to point to my manufacturer's sites, as well as update my doctors daily. I want to remind the new comers, this is for a total stationary packet. -business cards -note / thank you cards (no need for the actual words "Thank you") -note pads -letter head -fax cover sheet -folder -simple email signature -envelopes (both regular size and also 8.5" x 11" size for literature) I hope this helps. I will let the contest run its full length of time, then post my decision sometime Monday 1/13 CST. Thanks so much! Boris
Wow! Lots of design ideas very quickly. Please remember, I need more than business cards!!
Designers - For some reason my comments did not upload correctly. What you see on the brief was from an old project that was deleted. ***Please note the following items. >>> I need a complete stationary package - business cards, thank you cards (a MUST!), note pad, letter head, folders, etc. >>> I need the business cards in white. I would like the logo on the back, with possibly a "ghosted" version of the tooth on the logo, without the name on it, enlarged and on the back of the card as well. I do not need the comments about Harbor Cell or Vanta on the cards. Nor, do I need regenerative products or disposable surgical supplies on the card. >>> I need an editable version that I can add the website, facebook, and business email address to at a later date. >>> PLEASE CONTACT ME IF YOU HAVE ANY QUESTIONS. Thanks! Boris
I'm not sure how these two got separated. I want the logo first, then use it on the business cards and stationery. Sorry for any confusion.

```html
<!DOCTYPE html>
<html lang="en">
<head>
<meta charset="utf-8">
<title>Dental Crestline Works – Business Card</title>
<link href="https://fonts.googleapis.com/css2?family=Open+Sans:wght@400;600;700&display=swap" rel="stylesheet">
<style>
  :root {
    --page-bg: #e9eaec;
    --card-white: #ffffff;
    --brand-blue: #1c8fd6;
    --brand-blue-dark: #0d5fa3;
    --brand-navy: #1f2e6e;
    --silver-light: #e6e8ea;
    --silver-mid: #b9bdc2;
    --silver-dark: #8e9399;
    --text-grey: #5b6066;
    --text-white: #ffffff;
  }
  * { box-sizing: border-box; margin: 0; padding: 0; }
  html, body {
    width: 1200px; height: 600px; overflow: hidden;
    background: var(--page-bg);
    font-family: "Open Sans", Arial, sans-serif;
  }
  .stage { position: relative; width: 1200px; height: 600px; }

  .card {
    position: absolute; top: 150px;
    width: 520px; height: 300px;
    border-radius: 16px; overflow: hidden;
    box-shadow: 0 4px 14px rgba(0,0,0,0.15);
  }

  /* Front */
  .card-front { left: 50px; background: var(--card-white); }
  .front-brand {
    position: absolute; top: 78px; left: 80px;
    display: flex; align-items: center; gap: 12px;
  }
  .brand-dot {
    width: 30px; height: 30px; border-radius: 50%;
    background: var(--brand-blue);
  }
  .brand-name {
    font-size: 26px; font-weight: 700; color: var(--brand-blue-dark);
    letter-spacing: -0.3px;
  }
  .front-stripes { position: absolute; left: 0; top: 140px; width: 520px; height: 40px; }
  .front-lower {
    position: absolute; left: 0; top: 172px; width: 520px; height: 128px;
    background: linear-gradient(180deg, var(--silver-light) 0%, var(--silver-mid) 55%, var(--silver-dark) 100%);
  }
  .person-name {
    position: absolute; top: 26px; width: 100%; text-align: center;
    font-size: 17px; font-weight: 400; color: var(--text-grey);
  }
  .name-rule {
    position: absolute; top: 56px; left: 40px; right: 40px;
    height: 1px; background: rgba(255,255,255,0.7);
  }
  .contact-row {
    position: absolute; top: 76px; left: 0; width: 100%;
    display: flex; justify-content: center; gap: 22px;
    font-size: 9.5px; color: var(--text-white);
  }
  .contact-item { display: flex; align-items: center; gap: 5px; }
  .contact-item svg { width: 10px; height: 10px; }

  /* Back */
  .card-back {
    left: 630px;
    background: linear-gradient(160deg, #3aa6e6 0%, var(--brand-blue) 50%, var(--brand-blue-dark) 100%);
  }
  .back-art {
    position: absolute; top: 0; right: 0; width: 360px; height: 300px;
    background: radial-gradient(ellipse at 75% 30%, #f4f5f6 0%, #c9ccd0 45%, rgba(150,170,190,0.55) 70%, rgba(28,143,214,0) 90%);
  }
  .back-brand {
    position: absolute; left: 28px; bottom: 30px;
    transform-origin: left bottom;
    transform: rotate(-90deg) translateY(100%);
    font-size: 22px; font-weight: 700; color: var(--text-white);
    white-space: nowrap; letter-spacing: -0.2px;
  }
</style>
</head>
<body>
<main class="stage">

  <section class="card card-front" aria-label="Business card front">
    <div class="front-brand">
      <span class="brand-dot"></span>
      <span class="brand-name">Dental Crestline Works</span>
    </div>

    <svg class="front-stripes" viewBox="0 0 520 40" preserveAspectRatio="none" aria-hidden="true">
      <polygon points="0,16 520,4 520,10 0,22" fill="var(--brand-navy)"/>
      <polygon points="0,24 520,12 520,32 0,36" fill="var(--brand-blue)"/>
    </svg>

    <div class="front-lower">
      <p class="person-name">Boris Kestrow</p>
      <div class="name-rule"></div>
      <div class="contact-row">
        <span class="contact-item">
          <svg viewBox="0 0 10 10" aria-hidden="true"><path d="M2 1h2l1 2-1 1c.5 1 1 1.5 2 2l1-1 2 1v2c-4 1-8-3-7-7z" fill="#fff"/></svg>
          555 010 4827
        </span>
        <span class="contact-item">
          <svg viewBox="0 0 10 10" aria-hidden="true"><rect x="1" y="2" width="8" height="6" fill="none" stroke="#fff"/><path d="M1 2l4 3 4-3" fill="none" stroke="#fff"/></svg>
          boris.kestrow@fernmail.example
        </span>
        <span class="contact-item">
          <svg viewBox="0 0 10 10" aria-hidden="true"><circle cx="5" cy="5" r="4" fill="none" stroke="#fff"/><path d="M1 5h8M5 1v8" stroke="#fff"/></svg>
          www.dentalcrestlineworks.example
        </span>
      </div>
    </div>
  </section>

  <section class="card card-back" aria-label="Business card back">
    <div class="back-art" role="img" aria-label="Silver interlocking puzzle-piece artwork over blue"></div>
    <p class="back-brand">Dental Crestline Works</p>
  </section>

</main>
</body>
</html>
```